Square graphic for social media post

I want to create a 1080 x 1080px all-black image for the quote below that I can share on social media. I want the emphasis to be primarily on the quote, secondarily on the portrait, and third (smallest) on the logo. I want the background on the portrait to be edited so it's transparent and just shows the face of the person on a black background (no brick wall visible).

Graphic color: black
Text color: white
Content: "What we went through is going to make the greatest generation of hoteliers our industry has ever seen." << biggest text
Derek Holloway << smaller text
President, Ridgemont Hotels << smaller text
[image of person - use whichever version looks better to you]
[Add Lodging Ledger logo - whichever looks better to you]

This image needs to be readable when sized down much smaller (400x400?) so want the text and portrait to take up most of the space.

I'd like the output both as PNG and original file (preferably Canva). Thanks!

Target Market(s)

Hotel managers

Industry/Entity Type

Hospitality

Font styles to use
Sans Serif

Colors

Designer to choose colors to be used in the design.

Requirements
Must have
• Needs to focus on the quote and the person quoted (the portrait)

```html
<!DOCTYPE html>
<html lang="en">
<head>
<meta charset="UTF-8">
<title>Quote Post – Derek Holloway</title>
<link href="https://fonts.googleapis.com/css2?family=Rasa:wght@400;600;700&display=swap" rel="stylesheet">
<style>
  :root {
    --stage: #1b1c1f;
    --card: #050505;
    --ink: #ffffff;
    --motif: #f2f2f2;
    --portrait-light: #d9d9d9;
    --portrait-dark: #3a3a3a;
  }
  * { margin: 0; padding: 0; box-sizing: border-box; }
  html, body {
    width: 675px; height: 1200px; overflow: hidden;
    background: var(--stage);
  }
  .post {
    position: absolute; left: 17px; top: 280px;
    width: 640px; height: 640px;
    background: var(--card);
    color: var(--ink);
    font-family: "Rasa", Georgia, serif;
  }
  .motif-column { position: absolute; left: 0; top: 0; width: 193px; height: 100%; }
  .motif {
    position: absolute; left: 48px; width: 92px; height: 165px;
    background: var(--motif);
    border-radius: 46px 46px 40px 40px;
  }
  .motif--1 { top: 21px; }
  .motif--2 { top: 232px; }
  .motif--3 { top: 444px; }
  .divider {
    position: absolute; left: 193px; top: 5px;
    width: 2px; height: 621px; background: var(--ink);
  }
  .content { position: absolute; left: 195px; right: 0; top: 0; bottom: 0; text-align: center; }
  .brand {
    position: absolute; top: 62px; left: 0; right: 0;
    display: flex; align-items: center; justify-content: center; gap: 8px;
    font-size: 17px; font-weight: 600; letter-spacing: 3px; text-transform: uppercase;
  }
  .brand__dot { width: 7px; height: 7px; border-radius: 50%; background: var(--ink); }
  .portrait {
    position: absolute; left: 50%; top: 173px; transform: translateX(-50%);
    width: 166px; height: 166px; border-radius: 50%;
    border: 1.5px solid var(--ink);
    background: radial-gradient(circle at 50% 40%, var(--portrait-light) 0%, #9a9a9a 45%, var(--portrait-dark) 100%);
  }
  .quote {
    position: absolute; top: 366px; left: 0; right: 0;
    font-size: 26px; font-weight: 600; line-height: 35.5px;
  }
  .rule {
    position: absolute; top: 534px; left: 50%; transform: translateX(-50%);
    width: 267px; height: 1px; background: var(--ink);
  }
  .attribution { position: absolute; top: 548px; left: 0; right: 0; line-height: 28px; }
  .attribution__name { font-size: 19px; font-weight: 700; }
  .attribution__title { font-size: 19px; font-weight: 400; }
</style>
</head>
<body>
  <main class="post">
    <div class="motif-column">
      <div class="motif motif--1" role="img" aria-label="White pineapple illustration"></div>
      <div class="motif motif--2" role="img" aria-label="White pineapple illustration"></div>
      <div class="motif motif--3" role="img" aria-label="White pineapple illustration"></div>
    </div>
    <div class="divider"></div>
    <section class="content">
      <div class="brand"><span class="brand__dot"></span>Lodging Ledger</div>
      <div class="portrait" role="img" aria-label="Black and white portrait of Derek Holloway"></div>
      <p class="quote">"What we went through<br>is going to make the greatest<br>generation of hoteliers<br>our industry has ever seen."</p>
      <div class="rule"></div>
      <div class="attribution">
        <p class="attribution__name">Derek Holloway</p>
        <p class="attribution__title">President, Ridgemont Hotels</p>
      </div>
    </section>
  </main>
</body>
</html>
```